Business cards design on a high standard

We advise clients on insurance and financial matters, since these clients pay for our advice, the design should have a high standard. Our logo should be included. From the colors we are open for everything.

Colors

Designer to choose colors to be used in the design.

```html
<!DOCTYPE html>
<html lang="en">
<head>
<meta charset="utf-8">
<title>Kestrel Advisory – Business Cards</title>
<link rel="stylesheet" href="https://fonts.googleapis.com/css2?family=Roboto:wght@400;500;700&display=swap">
<style>
  :root {
    --bg: #2b2b2d;
    --red: #d90000;
    --red-deep: #c80000;
    --white: #ffffff;
    --grey: #9a9a9c;
    --ink: #ffffff;
  }
  * { margin: 0; padding: 0; box-sizing: border-box; }
  html, body { width: 1200px; height: 960px; overflow: hidden; background: var(--bg); }
  body { position: relative; font-family: "Roboto", Arial, sans-serif; }

  .card {
    position: absolute;
    width: 560px;
    height: 320px;
    overflow: hidden;
    box-shadow: 0 18px 40px rgba(0,0,0,0.45);
  }

  .card--front {
    left: 90px; top: 110px;
    background: var(--red-deep);
    display: flex; align-items: center; justify-content: center;
  }

  .card--back {
    left: 550px; top: 510px;
    background: var(--white);
  }

  .brand {
    font-weight: 700;
    font-size: 40px;
    letter-spacing: 2px;
    line-height: 1.05;
    text-transform: uppercase;
  }
  .brand__line { display: block; white-space: nowrap; }
  .card--front .brand { color: var(--white); }
  .card--back .brand {
    position: absolute;
    left: 56px; top: 96px;
    font-size: 36px;
    color: var(--red);
  }

  .back-wave { position: absolute; inset: 0; width: 100%; height: 100%; }

  .contact {
    position: absolute;
    right: 28px; top: 96px;
    text-align: right;
    color: var(--ink);
  }
  .contact__name { font-size: 20px; font-weight: 700; }
  .contact__title { font-size: 13px; font-weight: 500; margin-bottom: 18px; }
  .contact__line {
    font-size: 13px; line-height: 19px;
    display: flex; justify-content: flex-end; align-items: center; gap: 6px;
    white-space: nowrap;
  }
  .contact__address { margin-bottom: 6px; }
  .contact__line svg { width: 11px; height: 11px; fill: var(--white); }
</style>
</head>
<body>

  <section class="card card--front">
    <div class="brand">
      <span class="brand__line">Kestrel</span>
      <span class="brand__line">Advisory</span>
    </div>
  </section>

  <section class="card card--back">
    <svg class="back-wave" viewBox="0 0 560 320" preserveAspectRatio="none" aria-hidden="true">
      <path d="M560 0 L452 0 C380 6 372 110 338 190 C300 262 220 268 0 258 L0 320 L560 320 Z" fill="#e0e0e2"/>
      <path d="M560 0 L440 0 C368 6 360 110 326 188 C290 258 210 262 0 250" fill="none" stroke="var(--grey)" stroke-width="8"/>
      <path d="M560 0 L452 0 C378 6 370 112 334 192 C298 266 218 272 0 264" fill="none" stroke="var(--red)" stroke-width="2.5"/>
      <path d="M560 0 L462 0 C390 10 384 118 348 198 C310 272 230 280 0 272 L0 320 L560 320 Z" fill="var(--red)"/>
    </svg>

    <div class="brand">
      <span class="brand__line">Kestrel</span>
      <span class="brand__line">Advisory</span>
    </div>

    <div class="contact">
      <div class="contact__name">Daniel Hart</div>
      <div class="contact__title">President</div>
      <div class="contact__address">
        <div class="contact__line">412 Maple Court</div>
        <div class="contact__line">Fairview, Oregon 97024</div>
      </div>
      <div class="contact__line">555-014-2270
        <svg viewBox="0 0 24 24"><path d="M6.6 10.8a15.1 15.1 0 0 0 6.6 6.6l2.2-2.2a1 1 0 0 1 1-.25 11.4 11.4 0 0 0 3.6.57 1 1 0 0 1 1 1V20a1 1 0 0 1-1 1A17 17 0 0 1 3 4a1 1 0 0 1 1-1h3.5a1 1 0 0 1 1 1c0 1.25.2 2.45.57 3.57a1 1 0 0 1-.25 1z"/></svg>
      </div>
      <div class="contact__line">hello@kestreladvisory.com
        <svg viewBox="0 0 24 24"><path d="M2 5h20v14H2z M2 5l10 8 10-8" fill="none" stroke="#fff" stroke-width="2"/></svg>
      </div>
      <div class="contact__line">www.kestreladvisory.com
        <svg viewBox="0 0 24 24"><circle cx="12" cy="12" r="10"/></svg>
      </div>
    </div>
  </section>

</body>
</html>
```